The Harbor Lantern Showcase - needs a 32page Booklet---- Design to Press Ready

The Harbor Lantern Showcase in Australia is a mobile exhibition that seeks to promote the historical and contemporary understanding of the Bible. As most visitors are unable to absorb all of the information we want to provide an information booklet that they can take home and at their convenience.

We therefore require a 32 Page Booklet from design to press ready artwork.
Text is available from the attached work document. A few info-table graphics will need to be created. All other pictures and graphics will need to be extracts from existing files PDF or In-design files. (see attached brief for details)

The front cover will include the Exhibition Logo. It should also be a “clean” style.
The back page should also be ‘clean’ and have contact details inc. QR code
Internal pages: The booklet internal background should mainly be white, with colour used to enhance the feel, perhaps using consistent graphical elements throughout. (A few solid colour pages or background images would be acceptable).
Each page will be numbered at the bottom.
Generally pages will have text – the booklet is text heavy. Most pages will have one or two existing artwork elements. These will need to be extracted from existing exhibition panel artwork as indicated in the Graphic/pictures content document. These elements are available from both PDF and Indesign files. Due to their size the files are available at -
files.storelink-example.net/share/7Kq9vTz3LmW2xPa8RnB5yHd4Jc6?view=open
A two column text layout per single page is anticipated.
Font Style is - Geogrotesque Slab
The text content has some formatting applied eg bold, italics. This should be changed to reflect the deign proposed. We suggest that adopting the design for headings and colour scheme used in each section of the relevant exhibition panels

Target Market(s)

Harbor Lantern Showcase attendees

Requirements
Must have
• Press Ready Experience
• SEE DESIGN BRIEF FILE

```html
<!DOCTYPE html>
<html lang="en">
<head>
<meta charset="utf-8">
<title>The Harbor Lantern Showcase – Booklet Spreads</title>
<link rel="stylesheet" href="https://fonts.googleapis.com/css2?family=Roboto+Slab:wght@300;400;600;800&display=swap">
<style>
  :root{
    --board:#d6d6d6;
    --paper:#ffffff;
    --ink:#1d1d1d;
    --orange:#ee6a33;
    --purple:#6657ad;
    --teal:#1f6f86;
    --yellow:#f6c129;
    --rule:#7a7a7a;
    --coral:#f06545;
  }
  *{margin:0;padding:0;box-sizing:border-box}
  html,body{width:1200px;height:1200px;overflow:hidden;background:var(--board)}
  body{font-family:"Roboto Slab",serif;color:var(--ink)}
  .canvas{position:relative;width:1200px;height:1200px;overflow:hidden;background:var(--board)}

  .spread{position:absolute;left:18px;width:1162px;height:410px;background:var(--paper);box-shadow:4px 5px 6px rgba(0,0,0,.28)}
  .spread--top{top:27px}
  .spread--bottom{top:762px}
  .page{position:absolute;top:0;width:581px;height:410px}
  .page--left{left:0}
  .page--right{left:581px}
  .spread--top .page--left{border-right:1px solid #9a9a9a}
  .page--yellow{background:var(--yellow)}

  .el{position:absolute}
  .title{font-weight:800;color:var(--orange);font-size:21.5px;letter-spacing:.2px;line-height:1}
  .body{font-size:7.3px;line-height:10.4px;font-weight:400}
  .body p{margin-bottom:10.4px}
  .quote{color:var(--purple);font-weight:600;font-style:italic}
  .sub{color:var(--purple);font-weight:600;display:block}
  .caption{font-size:5.6px;font-weight:600;line-height:1}
  .bullet{color:var(--coral)}
  .photo{position:absolute}

  .footer{position:absolute;top:386px;font-size:5.6px;line-height:8px;display:flex;align-items:center;gap:5px}
  .footer .num{font-weight:600;padding-right:5px;border-right:1px solid var(--rule)}
  .footer--right .num{border-right:none;border-left:1px solid var(--rule);padding-right:0;padding-left:5px}
  .footer .brand{color:var(--teal)}

  .zoom{position:absolute;top:461px;width:274px;height:274px;border-radius:50%;overflow:hidden;background:var(--paper);box-shadow:3px 4px 6px rgba(0,0,0,.25)}
  .zoom--yellow{background:var(--yellow)}
  .zoom .z{position:absolute;white-space:nowrap}
</style>
</head>
<body>
<div class="canvas">

  <!-- Spread: pages 4–5 -->
  <section class="spread spread--top">
    <div class="page page--left">
      <h1 class="el title" style="left:28px;top:42px">Australia and the Bible</h1>
      <div class="photo" role="img" aria-label="Sepia photograph of a horse-drawn gospel wagon" style="left:28px;top:67px;width:256px;height:115px;background:linear-gradient(160deg,#b9a27a,#8e7752 60%,#a48c63)"></div>
      <div class="el caption" style="left:28px;top:187px">Donkey</div>
      <div class="el body" style="left:28px;top:200px;width:256px">
        <p><span class="quote">“Righteousness exalts a nation”</span> [Proverbs 14:34].</p>
        <p>The first Bible to arrive permanently in Australia came with the First Fleet in 1788. On 3 February 1788, the Chaplain, Richard Hallam, used it to read the following words to the people of the new colony:</p>
        <p><span class="quote">“What shall I render unto the Lord for all His benefits toward me?”</span> [Psalm 116:12]</p>
        <p>Well might Hallam use those words! God had safely brought almost 1500 people and their goods in 11 tiny sailing ships, over 15000 miles of wild ocean to a land only visited once before, with minimal loss of life! But we can only wonder – did Hallam direct the thoughts of his audience to the following words of Psalm 116:“I will take the cup of salvation, and call upon the name of the</p>
      </div>
      <div class="el body" style="left:298px;top:66px;width:256px">
        <p>Lord.” [Psalm 116:13]? Here, in the psalmist’s response to his own question, they could have found the key to successful nationhood and a successful individual life for all people. We will never know what he said!</p>
        <p style="margin-bottom:0">Nonetheless, it was a promising start! The presence of Hallam and his successors, during difficult early years, ensured all the convicts and soldiers knew of the importance of moral and spiritual uprightness. The early years of Australian history saw the arrival of fiery preachers such as Samuel Whitcombe [though a deeply conflicted individual], and more benevolent missionaries,</p>
      </div>
      <div class="el body" style="left:298px;top:211px;width:90px">who reached out with kindness to the wider, troubled community. Though Whitcombe and others found little response in the convicts, soldiers or the Aboriginal people, churches were constructed, and the convicts were</div>
      <div class="photo" role="img" aria-label="Old photograph of a couple standing beside a car carrying a gospel sign" style="left:393px;top:212px;width:74px;height:96px;background:linear-gradient(170deg,#cfcfcf,#7c7c7c 55%,#4a4a4a)"></div>
      <div class="el caption" style="left:393px;top:312px">Mr and Mrs S. Carrow</div>
      <div class="el body" style="left:298px;top:321px;width:256px">
        <p>required to attend these regularly.</p>
        <p>The society which progressively developed in Australia considered itself a “God-fearing”, Christian society, with a strong adherence to Biblical moral and ethical principles. However, there were many occasions in the early history when actions were taken which were very far from Biblical in origin. The treatment</p>
      </div>
      <div class="footer" style="left:30px"><span class="num">4</span><span class="brand">The Harbor Lantern Showcase</span><span>- Exploring The World’s Best-Selling Book</span></div>
    </div>

    <div class="page page--right">
      <div class="photo" role="img" aria-label="Black and white portrait of a young sailor in uniform" style="left:28px;top:67px;width:72px;height:110px;background:linear-gradient(180deg,#e4e4e4,#8a8a8a 45%,#2b2b2b)"></div>
      <div class="el caption" style="left:28px;top:183px">Frank Dellow</div>
      <div class="el body" style="left:106px;top:66px;width:180px">
        <p>of convicts in some places was oppressive and sadistic, and the dealings with the native peoples of the continent produced significant destruction of the indigenous people and their culture.</p>
        <p style="margin-bottom:0">Australia has traditionally been a nation which enjoyed civil and human rights which, while many fail to recognise it, remain firmly grounded in the ethical and moral principles taught by the Bible! There has continued to be a freedom to publicly preach and teach the</p>
      </div>
      <div class="el body" style="left:28px;top:211px;width:258px">truth of the Bible. Jesus taught His disciples that this was their great responsibility:</div>
      <div class="photo" role="img" aria-label="Photographs of a vintage green Bible van" style="left:28px;top:250px;width:256px;height:132px;background:linear-gradient(160deg,#6f8c6a,#2e5a3a 45%,#8d9a8f)"></div>
      <div class="el caption" style="left:28px;top:386px">Bible Van</div>
      <div class="photo" role="img" aria-label="Night view of the harbour opera house with an inset street portrait" style="left:298px;top:67px;width:257px;height:124px;background:linear-gradient(170deg,#3b3424,#17140f 55%,#6b5b33)"></div>
      <div class="el caption" style="left:298px;top:197px">Sydney Eternity&nbsp;&nbsp;[Inset: Mr Everlasting]</div>
      <div class="el body" style="left:298px;top:212px;width:257px">
        <p><span class="quote">“Go ye into all the world, and preach the gospel to every creature”</span> [Mark 16:15]</p>
        <p>Throughout the course of Australian history this work has continued, with Christians spreading the message of the Bible: a message which the God of the Bible wants all to hear and receive. So, by horseback, by aircraft, by motor vehicle, by post, by radio, by printed literature, by roadside displays, in formal meetings and face-to-face contacts, by personal conversation and bold public pronouncements – in many ways, the Bible and its message of salvation for humanity has been spread to the whole population, so that everyone can hear it.</p>
        <p>The spread of the message of the Bible continues to this day – and that summarises the role of this Harbor Lantern Showcase!</p>
      </div>
      <div class="footer footer--right" style="right:28px"><span class="brand">The Harbor Lantern Showcase</span><span>- Exploring The World’s Best-Selling Book</span><span class="num">5</span></div>
    </div>
  </section>

  <!-- Detail circles -->
  <div class="zoom" style="left:80px">
    <div class="photo" role="img" aria-label="Night harbour scene with lit opera house sails" style="left:0;top:0;width:274px;height:185px;background:linear-gradient(170deg,#5a4a25,#1c170e 50%,#3d3a2c)"></div>
    <div class="photo" role="img" aria-label="Black and white inset photo of a man writing in chalk" style="left:24px;top:37px;width:96px;height:150px;background:#fff;padding:4px">
      <div style="width:100%;height:100%;background:linear-gradient(180deg,#5b5b5b,#1e1e1e 55%,#8a8a8a)"></div>
    </div>
    <div class="z" style="left:28px;top:192px;font-size:10px;font-weight:600">Sydney Eternity&nbsp;&nbsp;&nbsp;[Inset: Mr Everlasting]</div>
    <div class="z" style="left:22px;top:223px;font-size:13.6px;line-height:18px"><span class="quote">“Go ye into all the world, and p</span><br><span class="quote">ature”</span> [Mark 16:15]</div>
  </div>

  <div class="zoom" style="left:455px">
    <div class="photo" role="img" aria-label="Close view of an old open book on a wooden printing press" style="left:0;top:0;width:274px;height:141px;background:linear-gradient(160deg,#3a2a1c,#1a120b 55%,#6b5037)"></div>
    <div class="z" style="left:-2px;top:149px;font-size:13.6px;line-height:18px;font-weight:300">Many readers might wonder where the Bi<br>ontains what it does, and why there are n<br>t us try to simply explain its origins.</div>
    <div class="z" style="left:30px;top:219px;font-size:13.6px;line-height:18px;font-weight:400"><span class="sub">Bible was Written by Men ...</span><span style="font-weight:300">lish word “bible” is derive<br>“the books”. It wa</span></div>
  </div>

  <div class="zoom zoom--yellow" style="left:829px">
    <div class="z" style="left:38px;top:20px;font-size:15px;font-weight:600;color:var(--purple)">Who has the Original Text</div>
    <div class="z" style="left:40px;top:40px;font-size:15px;line-height:20px;font-weight:300">The original writings have lo<br>dependent upon copies of these<br>scribes. The scribes used variou<br>including counting paragraphs,<br>Many old manuscripts in the orig<br>Here are just a few examples, wh<br>Bibles:</div>
    <div class="z" style="left:40px;top:205px;font-size:15px;line-height:20px;font-weight:300"><span class="bullet">• DEAD SEA SCROLLS [QUMRA</span><br>&nbsp;&nbsp;manuscript discovery of a</div>
  </div>

  <!-- Spread: pages 6–7 -->
  <section class="spread spread--bottom">
    <div class="page page--left">
      <h1 class="el title" style="left:28px;top:26px">The Origins of the Bible</h1>
      <div class="photo" role="img" aria-label="Dim photograph of a historic wooden printing press with a printed sheet" style="left:28px;top:66px;width:256px;height:204px;background:linear-gradient(160deg,#4a3523,#1d140c 55%,#7a5a3c)"></div>
      <div class="el body" style="left:28px;top:276px;width:256px">
        <p>Many readers might wonder where the Bible came from, why it contains what it does, and why there are numerous translations. Let us try to simply explain its origins.</p>
        <p><span class="sub">The Bible was Written by Men ...</span>The English word “bible” is derived from the Greek ta <i>biblia</i>, which means “the books”. It was prepared over a period of history covering some 1600 years, and contributed to by over 40</p>
      </div>
      <div class="el body" style="left:298px;top:66px;width:256px">
        <p>individuals. It is divided into two parts: the Old Testament [OT] and the New Testament [NT].</p>
        <p>The Old Testament is comprised of 39 separate books and presents God’s dealings with Israel, written in the ancient Hebrew and Aramaic languages. The New Testament contains 27 books and records the coming of Jesus and the teaching of the Christian faith. It was written in Koine Greek [“common Greek”] over a few decades in the first century AD</p>
        <p><span class="sub">... but its Source was from God.</span>The words of the Bible are the words of God Himself. The Bible says, <i>“All scripture is given by inspiration of God”</i> [2 Timothy 3:16]. This means that the “Scripture”, the OT and the NT, was “breathed by God”. What an astonishing thing! When we read the words of the Bible, we are reading the words which God has said!</p>
        <p><span class="sub">How did it become a Single Volume?</span>When the books of the OT were prepared they were handwritten in separate scrolls, which were then continually copied by hand. Many of the NT books took the form of letters to individuals and groups, who were often widely scattered geographically.<br>In the first century BC [Before Christ], the long process of compiling a single volume of OT books was completed. This became the Hebrew Bible [the Tanakh], the precursor to the OT. The NT was added by early church fathers, and after much thoughtful consideration, the books which we have now were incorporated in 360AD.</p>
      </div>
      <div class="footer" style="left:30px"><span class="num">6</span><span class="brand">The Harbor Lantern Showcase</span><span>- Exploring The World’s Best-Selling Book</span></div>
    </div>

    <div class="page page--right page--yellow">
      <div class="el body" style="left:28px;top:66px;width:258px">
        <p><span class="sub">How were its Contents Decided?</span>The key consideration of the ancient scholars was whether they could be satisfied that the individuals who wrote the books were indeed <i>“inspired”</i> by God. The process of making a decision about which books were inspired became known as “canonisation”. [“Canonisation” derives from a Greek word meaning “a measuring stick”]. The Bible canon is now closed, as the revelation of God has been completed forever.</p>
        <p><span class="sub">Why is there an Old Testament and a New Testament?</span>The word “testament” means a covenant or a formal agreement. The OT describes a number of covenants. The most notable of these was the Law [including the Ten Commandments], which detailed God’s standards. The NT sets out a “new covenant”, which promises <i>“forgiveness of sins”</i> based only on the death of Jesus on the Cross.</p>
        <p><span class="sub">Who has the Original Texts?</span>The original writings have long since been lost. We are now dependent upon copies of these, painstakingly handwritten by scribes. The scribes used various techniques to ensure accuracy, including counting paragraphs, lines, words and letter details. Many old manuscripts in the original languages do remain. Here are just a few examples, which have contributed to modern Bibles:</p>
        <p><span class="bullet">• DEAD SEA SCROLLS [QUMRAN SCROLLS] –</span> perhaps the greatest manuscript discovery of all time, these were uncovered in caves</p>
      </div>
      <div class="el body" style="left:303px;top:66px;width:252px">
        <p>in the Judean desert near the Dead Sea. Recovered from 1946 to the present, the Dead Sea Scrolls consist of some 981 individual manuscripts. The ages of the scrolls range from the 8th century BC to the 11th CENTURY AD, AND THE DISCOVERY INCLUDES MULTIPLE COPIES AND FRAGMENTS OF MOST OT BOOKS.<br><span class="bullet">• CODEX SINAITICUS –</span> discovered in a monastery in the Sinai Peninsula in the 19th century AD, and dating from the 4th century AD, this is one of the oldest Greek manuscripts of the full Bible, although some short sections are missing.<br><span class="bullet">• CODEX VATICANUS –</span> in the possession of the Vatican Library, this is also considered one of the oldest surviving copies of the Bible in Greek, although small sections are again missing. It dates from the 4th century AD.<br><span class="bullet">• CODEX ALEXANDRINUS –</span> discovered in the Egyptian city of Alexandria, it is believed to date from the 5th century AD, and contains all the books of the Bible in Greek, although yet again a few short sections are missing.</p>
        <p>Particular mention needs to be made of a manuscript known as the <i>Textus Receptus</i> [Latin for “received text”, TR]. Essentially, the TR is the first Greek manuscript of the Bible ever printed [as opposed to hand copied], and distributed in a printed form. It was prepared by a Dutch scholar, Desmond Aldous, and first printed in 1516. It became the dominant Greek text for the next two or three centuries.<br>It is important to note that while some variations occur from one ancient manuscript to another, these variations are insignificant</p>
      </div>
      <div class="footer footer--right" style="right:28px"><span class="brand">The Harbor Lantern Showcase</span><span>- Exploring The World’s Best-Selling Book</span><span class="num">7</span></div>
    </div>
  </section>

</div>
</body>
</html>
```